High-end law practice specializing in closely held business succession planning and complex estates

Solo practitioner whose practice specializes in high-net worth, complex estate planning needs muliple versions of letterhead black and white, please. Letterhead should incorporate slogan, "Protecting your family business is my business," for one and "Complex Estate Planning"; third with no slogan. All for The Law Office of Marnie Kate Wexford, PC, 418 Corlow Bend Rd., Newport News, Virginia 23694, Tel. 757-468-1950 Fax tbd email: marnie@mkwcounsel.example; Marnie Kate Wexford, Esq., principal, licensed in VA, NY, DC
Updates

Project Deadline Extended
Reason: My internet service went down and I can only view designs on my smart phone -- it's just too hard to review. So sorry! Working with my ISP now. Please be patient!

Target Market(s)

High net worth clients with complex estate planning needs, family businesses, family farmers, family foresters -- people with unique estate/succession planning needs who need a specialist who understands them.

Industry/Entity Type

Business

Font styles to use
Script

Requirements
Must have
• A high-end look and feel, connoting trustworthiness, special knowledge, and expertise.

```html
<!DOCTYPE html>
<html lang="en">
<head>
<meta charset="utf-8">
<title>Letterhead – The Law Office of Marnie Kate Wexford, PC</title>
<link rel="stylesheet" href="https://fonts.googleapis.com/css2?family=Bitter:wght@300;400;700&display=swap">
<style>
  :root {
    --ink: #333132;
    --ink-soft: #4a4849;
    --paper: #ffffff;
    --icon-tone: #e6e6e6;
  }
  * { margin: 0; padding: 0; box-sizing: border-box; }
  html, body {
    width: 848px; height: 1200px; overflow: hidden; background: var(--paper);
  }
  .letterhead {
    position: relative; width: 848px; height: 1200px; overflow: hidden;
    background: var(--paper); color: var(--ink);
    font-family: "Bitter", Georgia, serif;
    border: 1px solid #cfcfcf;
  }
  .brand-mark {
    position: absolute; left: 36px; top: 58px;
    width: 92px; height: 92px; border-radius: 50%;
    border: 3px solid var(--ink);
  }
  .firm-intro {
    position: absolute; left: 171px; top: 63px;
    font-size: 23px; font-weight: 300; color: var(--ink-soft); line-height: 1;
  }
  .firm-name {
    position: absolute; left: 171px; top: 94px;
    font-size: 22px; font-weight: 700; line-height: 1; white-space: nowrap;
  }
  .firm-credentials {
    position: absolute; left: 171px; top: 126px;
    font-size: 12.5px; font-weight: 400; color: var(--ink-soft);
  }
  .practice-icons {
    position: absolute; left: 462px; top: 40px; width: 358px; height: 38px;
  }
  .slogan-bar {
    position: absolute; left: 449px; top: 93px; width: 381px; height: 24px;
    background: var(--ink); color: var(--paper);
    font-size: 15px; line-height: 24px; padding-left: 8px; white-space: nowrap;
  }
  .practice-areas {
    position: absolute; left: 452px; top: 120px;
    font-size: 13.5px; line-height: 18px; color: var(--ink); white-space: nowrap;
  }
  .practice-areas .sep { padding: 0 4px; }
  .footer-band {
    position: absolute; left: 0; bottom: 0; width: 848px; height: 150px; display: block;
  }
  .footer-contact {
    position: absolute; left: 0; top: 1132px; width: 848px;
    color: var(--paper); text-align: center; font-style: normal;
    font-size: 13.5px; line-height: 27px; white-space: nowrap;
  }
  .footer-contact .sep { padding: 0 4px; }
</style>
</head>
<body>
<main class="letterhead">
  <header>
    <div class="brand-mark" aria-hidden="true"></div>
    <p class="firm-intro">The Law Office of</p>
    <h1 class="firm-name">Marnie Kate Wexford, PC</h1>
    <p class="firm-credentials">Esq., principal, licensed in VA, NY, DC</p>

    <svg class="practice-icons" viewBox="0 0 358 38" role="img" aria-label="Row of line icons for legal practice: oath, scales, gavel, accounts, family, passport and handshake">
      <rect x="0" y="0" width="358" height="38" fill="var(--icon-tone)"/>
    </svg>

    <p class="slogan-bar">Protecting your family business is my business.</p>
    <p class="practice-areas">
      Estate Planning<span class="sep">|</span>Family Businesses<span class="sep">|</span>Family Farmers<br>
      Family Foresters<span class="sep">|</span>Unique Estate/Succession
    </p>
  </header>

  <footer>
    <svg class="footer-band" viewBox="0 0 848 150" preserveAspectRatio="none" aria-hidden="true">
      <path d="M0 62 C 300 64, 650 48, 848 0 L848 150 L0 150 Z" fill="var(--ink)"/>
    </svg>
    <address class="footer-contact">
      Address: 418 Corlow Bend Rd., Newport News, Virginia 23694,<br>
      Telephone: 757-468-1950<span class="sep">|</span>Fax: 757-555-0147<span class="sep">|</span>E-mail: marnie@mkwcounsel.example<span class="sep">|</span>Website: www.mkwcounsel.example
    </address>
  </footer>
</main>
</body>
</html>
```